Infographic for council approvals process

Looking to show the different steps that a person needs to undertake to get local council approval for their new swimming pool. It's a bit convoluted and text heavy when written out, but could be more graphically illustrated as a series of steps and choices.
Needs to be aligned to the brand for www.LagoonBasinSupply.com.au

Target Market(s)

Home Owners

Font styles to use
Sans Serif

Requirements
Must have
• Nice graphics that help simplify and layout the process graphically, the infographic should reference our brand colours and logos.

```html
<!DOCTYPE html>
<html lang="en">
<head>
<meta charset="utf-8">
<title>Council Approvals Process – Lagoon Basin Supply</title>
<link href="https://fonts.googleapis.com/css2?family=Exo+2:wght@700;800&family=Open+Sans:wght@400;600;700&display=swap" rel="stylesheet">
<style>
  :root{
    --stage:#031a33;
    --navy:#0b3a5c;
    --teal:#6fcad0;
    --teal-soft:#a6e3e6;
    --white:#ffffff;
    --ink:#1d2a33;
    --line:#c9d2d8;
    --sand:#f6c9a2;
    --pool:#7fd6de;
    --leaf:#3aa35a;
  }
  *{box-sizing:border-box;margin:0;padding:0}
  html,body{width:1200px;height:1200px;overflow:hidden;background:var(--stage)}
  body{font-family:"Open Sans",Arial,sans-serif;color:var(--ink);position:relative}
  .infographic{position:absolute;left:310px;top:20px;width:580px;height:1160px;background:var(--white);overflow:hidden}
  .band{position:absolute;left:0;width:100%}
  .band--header{top:0;height:170px;background:var(--navy)}
  .band--teal-1{top:290px;height:60px;background:var(--teal)}
  .band--teal-2{top:520px;height:70px;background:var(--teal)}
  .band--teal-3{top:870px;height:50px;background:var(--teal)}
  .band--footer{bottom:0;height:40px;background:var(--navy)}
  .title{position:absolute;right:34px;top:30px;text-align:right;font-family:"Exo 2",Arial,sans-serif;color:var(--white);line-height:1}
  .title__kicker{display:block;font-size:30px;font-weight:700;letter-spacing:1px}
  .title__main{display:block;font-size:50px;font-weight:800;letter-spacing:2px;margin-top:6px}
  .card{position:absolute;background:var(--white);border-radius:10px;padding:12px 14px;box-shadow:0 2px 6px rgba(0,0,0,.08)}
  .card__heading{font-family:"Exo 2",Arial,sans-serif;font-weight:700;font-size:11.5px;text-transform:uppercase;margin-bottom:7px}
  .card__body{border:1px solid var(--line);border-radius:8px;padding:8px 10px;font-size:9px;line-height:1.4}
  .card__body--center{text-align:center}
  .card__body--justify{text-align:justify}
  .bubble{position:absolute;background:var(--white);border:1px solid var(--line);border-radius:8px;padding:8px 10px;font-size:11px;font-weight:600;line-height:1.3}
  .bubble::after{content:"";position:absolute;bottom:-7px;left:40px;width:12px;height:12px;background:var(--white);border-right:1px solid var(--line);border-bottom:1px solid var(--line);transform:rotate(45deg)}
  .art{position:absolute;border-radius:14px}
  .art--pool{background:linear-gradient(135deg,var(--sand) 0%,var(--pool) 35%,var(--teal-soft) 100%)}
  .art--scene{background:linear-gradient(160deg,var(--teal-soft) 0%,#eef4f4 60%,var(--sand) 100%)}
  .art--palm{background:linear-gradient(180deg,var(--leaf) 0%,#c8924a 100%);border-radius:40px}
  .tips{list-style:none;counter-reset:tip}
  .tips li{margin-bottom:6px}
  .tips li span{font-weight:700}
</style>
</head>
<body>
<main class="infographic">
  <div class="band band--header"></div>
  <div class="band band--teal-1"></div>
  <div class="band band--teal-2"></div>
  <div class="band band--teal-3"></div>
  <div class="band band--footer"></div>

  <h1 class="title"><span class="title__kicker">COUNCIL APPROVALS</span><span class="title__main">PROCESS</span></h1>

  <div class="art art--pool" style="left:18px;top:130px;width:230px;height:150px" role="img" aria-label="Isometric illustration of a rectangular pool with a woman, palm tree and sun lounger"></div>

  <section class="card" style="left:262px;top:180px;width:300px">
    <h2 class="card__heading">Council approval for a pool in NSW</h2>
    <p class="card__body card__body--center">In NSW, every new pool construction must receive approval from a Licensed Certifier. Depending on the specific circumstances, some pools may need a Complying Development (CDC), while others will need a Development Application (DA) approval from the council.</p>
  </section>

  <section class="card" style="left:16px;top:330px;width:180px">
    <h2 class="card__heading">Option 1: CDC</h2>
    <p class="card__body">Most customers prefer to apply for a CDC as it is a faster, cheaper and straightforward process with a private certifier instead of the local council. In order to apply for a CDC, certain criteria need to be met. Make sure you look at this criteria to ensure you are eligible.</p>
  </section>

  <div class="art art--scene" style="left:206px;top:300px;width:170px;height:200px" role="img" aria-label="Illustration of a shaped pool with a woman relaxing on a sun lounger"></div>

  <section class="card" style="left:384px;top:330px;width:180px">
    <h2 class="card__heading" style="text-align:right">Option 2: DA</h2>
    <p class="card__body card__body--center">If you don't meet the requirements for a CDC, you'll need to obtain development consent from your local Council by submitting a Development Application (DA). This is the sole approval pathway in certain scenarios, such as if you're building a new home. Unfortunately this is a longer and more expensive process, so make sure you get this underway as soon as possible.</p>
  </section>

  <div class="bubble" style="left:30px;top:545px;width:150px">What do I need to do to get my pool approved?</div>

  <div class="art art--scene" style="left:20px;top:615px;width:230px;height:170px" role="img" aria-label="Illustration of a woman on a lounger talking with a pool consultant holding a clipboard"></div>

  <section class="card" style="left:262px;top:610px;width:300px">
    <p class="card__body card__body--justify">Navigating the planning requirements for installing a swimming pool can be a complex process, varying significantly across different Australian states. In New South Wales (NSW), Queensland (QLD), Victoria (VIC), and the Australian Capital Territory (ACT), understanding the specific regulations and procedures is crucial for a successful project. Each state has its own approval process, required permits, compliance standards, and inspection procedures.</p>
  </section>

  <section class="card" style="left:16px;top:800px;width:300px">
    <p class="card__body card__body--justify">When you're fibreglass pool and pool fence is installed, you'll be ready for a pool inspection. This is the last stage of the pool approval journey. An inspector will visit the site and ensure all regulations have been met. The inspector will conduct inspections, measurements, tests, and capture photographs of your pool gates, pool fences, dividing fences utilised as pool fences, and any objects or structures in close proximity to the pool fence.</p>
  </section>

  <div class="bubble" style="left:400px;top:780px;width:160px">What happens after my pool is installed?</div>

  <div class="art art--scene" style="left:330px;top:845px;width:230px;height:100px" role="img" aria-label="Illustration of a couple standing beside an oval pool"></div>

  <div class="art art--pool" style="left:18px;top:960px;width:190px;height:160px" role="img" aria-label="Illustration of a curved freeform pool with a palm tree"></div>

  <section class="card" style="left:218px;top:950px;width:346px">
    <h2 class="card__heading">Tips for successfully navigating planning requirements</h2>
    <ol class="card__body tips">
      <li><span>1.</span> Thoroughly research and understand local regulations. Take the time to familiarise yourself with the planning requirements in your area to ensure compliance.</li>
      <li><span>2.</span> Seek professional guidance when needed. If you encounter complexities, don't hesitate to consult professionals who can handle the approval process for you.</li>
      <li><span>3.</span> Complete all necessary paperwork accurately and on time, as delays or errors in paperwork can prolong the approval process.</li>
      <li><span>4.</span> Stay informed about any updates or changes to regulations and keep in touch with your local Council.</li>
    </ol>
  </section>
</main>
</body>
</html>
```